Exclusive British Dental Clinic Needs Modern Brochure to Attract New Patients

We are looking to create a smart, sophisticated brochure that gives the public and future potential clients a concise overview of what we offer and why the quality and care on offer is a step above the rest. We are based in the United Kingdom where the Public Wellness Board provide dental care free or at low cost. We are NOT an PWB provider. We are a wholly private dental clinic so all of our patients are paying full-price premium prices directly out of pocket. The work we do is exceptional so all of our patients can be assured that anything we do is done to the highest and best quality possible.
We offer high quality dental treatment using the best and latest techniques, materials and an award winning dental laboratory. All treatments are undertaken using high quality magnification to ensure the best possible result. We have over 30 years’ experience in general dentistry with fully trained staff. In quality comfortable surroundings, we are a caring practice with excellent patient care. We allow more time with our patients and we understand and care for nervous patients.
We also offer facial fillers, wrinkle reducers and teeth whitening in order to help our patients achieve their best look.

We have attached our logo and logo icons to this brief.
We also have attached some information in our Brochure Details document. This just highlights what we would like to see and more information about us.
We are really up to suggestion with design and wording because we want this brochure to be attractive and appealing to the public.
Feel free to edit as you see fit to help us attain our goals :)

Reason: Hello We are very excited about the work we have received thus far...our Practice Manager is away for the next week and we wanted to make sure we are all on board for the discussions and decisions we make moving forward. Thank you for taking the time to help us create our voice! --- Larkmoor Atelier Dental Clinic

```html
<!DOCTYPE html>
<html lang="en">
<head>
<meta charset="utf-8">
<title>Larkmoor Atelier Dental Clinic – Brochure Outside Spread</title>
<link href="https://fonts.googleapis.com/css2?family=Open+Sans:wght@400;600;700&display=swap" rel="stylesheet">
<style>
  :root {
    --bg: #e4e6e8;
    --paper: #ffffff;
    --green: #8cc63f;
    --teal: #2fae9b;
    --orange: #f58a1f;
    --sky: #3d9ad6;
    --sky-light: #bfe3f5;
    --ink: #4a4f55;
    --ink-soft: #8a9096;
    --blue-text: #1f6fa8;
  }
  * { margin: 0; padding: 0; box-sizing: border-box; }
  html, body {
    width: 900px; height: 1200px; overflow: hidden;
    background: var(--bg);
    font-family: "Open Sans", Arial, sans-serif;
    color: var(--ink);
  }
  .spread {
    position: absolute; left: 30px; top: 290px;
    width: 840px; height: 620px;
    display: flex; background: var(--paper);
    box-shadow: 0 8px 24px rgba(0,0,0,.15);
  }
  .panel { position: relative; width: 280px; height: 100%; overflow: hidden; }
  .panel + .panel { border-left: 1px solid #eceeef; }

  /* Contact panel */
  .treatment-photo {
    height: 230px;
    background: linear-gradient(135deg, #cfe6ee 0%, #8fc4d6 45%, #e8d8cc 100%);
  }
  .about-band { height: 120px; background: var(--green); padding: 18px 22px; color: #fff; }
  .about-band h2 { font-size: 17px; font-weight: 700; margin-bottom: 8px; }
  .about-band p { font-size: 11px; line-height: 1.55; }
  .contact-block { height: 270px; background: var(--teal); padding: 22px; color: #fff; }
  .contact-block h2 { font-size: 17px; font-weight: 700; font-style: italic; margin-bottom: 12px; }
  .contact-block ul { list-style: none; font-size: 11px; line-height: 2; }

  /* Map panel */
  .location-map {
    height: 300px;
    background: linear-gradient(160deg, #f1efe8 0%, #e6e3d8 50%, #f4e7b8 100%);
  }
  .map-lower { height: 320px; background: linear-gradient(180deg, var(--green) 0 14px, var(--teal) 14px); }

  /* Cover panel */
  .cover { display: flex; flex-direction: column; }
  .clinic-name {
    display: flex; align-items: center; gap: 10px;
    padding: 26px 22px 20px;
  }
  .clinic-name .mark { width: 28px; height: 28px; border-radius: 50%; background: var(--teal); flex: none; }
  .clinic-name span {
    font-size: 13px; font-weight: 600; letter-spacing: .08em;
    text-transform: uppercase; color: var(--teal); line-height: 1.3;
  }
  .smile-photo {
    height: 180px;
    background: linear-gradient(90deg, #e9b7a8 0%, #f4ece6 45%, var(--sky-light) 70%, var(--sky) 100%);
  }
  .tile-grid {
    display: grid; grid-template-columns: 1fr 1fr; grid-template-rows: 78px 78px;
    gap: 6px; padding: 6px 0 0 70px;
  }
  .tile-orange { background: var(--orange); }
  .tile-smile { background: linear-gradient(135deg, #c9463f, #f1d6cc 60%, #ffffff); }
  .tile-green { background: var(--green); }
  .tile-sky { background: linear-gradient(180deg, var(--sky), var(--sky-light)); }
  .cover-text { text-align: right; padding: 22px 20px 0; }
  .tagline { font-size: 13px; color: var(--ink-soft); }
  .phone { font-size: 22px; font-weight: 700; color: var(--blue-text); margin-top: 2px; }
  .web { font-size: 11px; color: var(--ink-soft); margin-top: 2px; }
  .cover-foot { margin-top: auto; height: 26px; background: var(--green); }
</style>
</head>
<body>
  <main class="spread">
    <section class="panel contact-panel">
      <div class="treatment-photo" role="img" aria-label="Photo of a dentist treating a smiling patient in the chair"></div>
      <div class="about-band">
        <h2>Who We Are</h2>
        <p>Private dental care with time, skill and calm for every patient.</p>
      </div>
      <div class="contact-block">
        <h2>Contact Information</h2>
        <ul>
          <li>12 Larkmoor Lane, Ashbridge</li>
          <li>Tel: 01632 960 481</li>
          <li>info@larkmooratelier.co.uk</li>
          <li>www.larkmooratelier.co.uk</li>
          <li>Mon–Sat 8am–6pm</li>
        </ul>
      </div>
    </section>

    <section class="panel map-panel">
      <div class="location-map" role="img" aria-label="Street map showing the clinic location"></div>
      <div class="map-lower"></div>
    </section>

    <section class="panel cover">
      <div class="clinic-name">
        <div class="mark"></div>
        <span>Larkmoor Atelier<br>Dental Clinic</span>
      </div>
      <div class="smile-photo" role="img" aria-label="Close-up photo of a bright white smile against blue sky"></div>
      <div class="tile-grid">
        <div class="tile-orange"></div>
        <div class="tile-smile" role="img" aria-label="Close-up photo of white teeth and red lips"></div>
        <div class="tile-green"></div>
        <div class="tile-sky" role="img" aria-label="Photo of blue sky and sea"></div>
      </div>
      <div class="cover-text">
        <p class="tagline">Central for Dental Excellence</p>
        <p class="phone">Call Us 01632 960 481</p>
        <p class="web">www.larkmooratelier.co.uk</p>
      </div>
      <div class="cover-foot"></div>
    </section>
  </main>
</body>
</html>
```